Willow Crossing: A Self Care Session for Employees

I need a flyer for organizations and businnesses. I am offering a session that will address behavioral issues such as coming to work late, not getting along with others and not working together as a team. I am a life coach who works with difficult employees, helping them address their issues and helping them be a better version of themselves. I also offer a leadership class for managers. I would like the flyer to be professional, clean and convey a feeling of trust. I would prefer to see disgns that use the color blue.

Target Market(s)

small businesses

Industry/Entity Type

Work

Font styles to use
Sans Serif

Colors
34a7d8
85cae6
0792cd
ffffff

Requirements
Must have
• shades of blue and perhaps white. should be clean, fresh and professional
Nice to have
• simple yet warm
Should not have
• distracting and heavy, playful

```html
<!DOCTYPE html>
<html lang="en">
<head>
<meta charset="utf-8">
<title>Willow Crossing – Self Care Session Flyer</title>
<link href="https://fonts.googleapis.com/css2?family=Lato:wght@400;700&family=Oswald:wght@600&display=swap" rel="stylesheet">
<style>
  :root {
    --blue-deep: #0792cd;
    --blue-mid: #34a7d8;
    --blue-light: #85cae6;
    --white: #ffffff;
    --ink: #333333;
    --heading-grey: #555555;
    --band-grey: #8a8a8a;
    --stage: #e9edf0;
    --photo-warm-dark: #4a3526;
    --photo-warm-light: #c8a27a;
  }
  html, body {
    margin: 0;
    padding: 0;
    width: 1200px;
    height: 1200px;
    overflow: hidden;
    background: var(--stage);
  }
  .flyer {
    position: absolute;
    left: 136px;
    top: 0;
    width: 842px;
    height: 1089px;
    transform: scale(1.1019);
    transform-origin: top left;
    background: var(--white);
    overflow: hidden;
    font-family: "Lato", sans-serif;
  }
  .flyer-shapes {
    position: absolute;
    inset: 0;
  }
  .brand {
    position: absolute;
    left: 118px;
    top: 120px;
    display: flex;
    align-items: center;
    gap: 10px;
    font-family: "Lato", sans-serif;
    font-weight: 700;
    font-size: 22px;
    line-height: 1.15;
    color: var(--blue-mid);
  }
  .brand-dot {
    width: 30px;
    height: 30px;
    border-radius: 50%;
    background: var(--blue-mid);
    flex: none;
  }
  .headline {
    position: absolute;
    left: 485px;
    top: 600px;
    margin: 0;
    font-family: "Oswald", sans-serif;
    font-weight: 600;
    font-size: 32px;
    line-height: 40px;
    text-transform: uppercase;
    color: var(--blue-deep);
  }
  .headline .lead {
    color: var(--heading-grey);
    display: block;
  }
  .points {
    position: absolute;
    left: 478px;
    top: 746px;
    width: 340px;
    margin: 0;
    padding: 0;
    list-style: none;
    font-size: 18px;
    line-height: 23px;
    color: var(--ink);
  }
  .points li {
    position: relative;
    padding-left: 35px;
    margin-bottom: 23px;
  }
  .points svg {
    position: absolute;
    left: 0;
    top: 3px;
    width: 20px;
    height: 20px;
  }
  .cta {
    position: absolute;
    left: 38px;
    top: 895px;
    margin: 0;
    font-weight: 700;
    font-size: 60px;
    line-height: 72px;
    color: var(--white);
  }
  .contact {
    position: absolute;
    left: 40px;
    top: 1000px;
    margin: 0;
    font-weight: 700;
    font-size: 24px;
    line-height: 30px;
    color: var(--white);
  }
  .contact svg {
    width: 22px;
    height: 22px;
    vertical-align: -4px;
    margin: 0 10px 0 14px;
  }
</style>
</head>
<body>
<main class="flyer">
  <svg class="flyer-shapes" viewBox="0 0 842 1089" width="842" height="1089">
    <defs>
      <linearGradient id="portraitTone" x1="0" y1="0" x2="1" y2="0">
        <stop offset="0" stop-color="#ffffff"/>
        <stop offset="0.12" stop-color="var(--photo-warm-light)"/>
        <stop offset="0.55" stop-color="var(--photo-warm-dark)"/>
        <stop offset="1" stop-color="#2f241c"/>
      </linearGradient>
      <linearGradient id="panelTone" x1="0" y1="0" x2="0" y2="1">
        <stop offset="0" stop-color="#4aaedb"/>
        <stop offset="0.6" stop-color="var(--blue-light)"/>
        <stop offset="1" stop-color="#2b4aa8"/>
      </linearGradient>
      <linearGradient id="footerTone" x1="0" y1="0" x2="0" y2="1">
        <stop offset="0" stop-color="var(--blue-deep)"/>
        <stop offset="1" stop-color="var(--blue-mid)"/>
      </linearGradient>
    </defs>
    <polygon role="img" aria-label="Portrait photo of the coach, smiling, in a warm interior"
      points="360,0 842,0 842,500 635,540 360,385" fill="url(#portraitTone)"/>
    <polygon role="img" aria-label="Photo of a woman in a blue top resting her head on her hand against a blue backdrop"
      points="0,200 505,492 395,880 0,880" fill="url(#panelTone)"/>
    <polygon class="footer-band" points="0,988 392,988 450,940 690,1089 0,1089" fill="url(#footerTone)"/>
    <polygon class="footer-grey" points="562,1002 842,1002 842,1089 690,1089" fill="var(--band-grey)"/>
    <polygon class="cta-band" points="0,885 390,885 442,932 390,978 0,978" fill="var(--blue-deep)" stroke="var(--white)" stroke-width="4"/>
  </svg>

  <div class="brand">
    <span class="brand-dot"></span>
    <span>Brightpath<br>Coaching Institute</span>
  </div>

  <h1 class="headline"><span class="lead">Willow Crossing:</span>A Self Care Session<br>for Employees</h1>

  <ul class="points">
    <li><svg viewBox="0 0 20 20"><circle cx="10" cy="10" r="8" fill="none" stroke="var(--blue-deep)" stroke-width="1.8"/><path d="M6 10.5l3 3 6-7" fill="none" stroke="var(--blue-deep)" stroke-width="1.8"/></svg>Are your employees bringing personal issues on the job?</li>
    <li><svg viewBox="0 0 20 20"><circle cx="10" cy="10" r="8" fill="none" stroke="var(--blue-deep)" stroke-width="1.8"/><path d="M6 10.5l3 3 6-7" fill="none" stroke="var(--blue-deep)" stroke-width="1.8"/></svg>Is it affecting team communication or may be even productivity?</li>
    <li><svg viewBox="0 0 20 20"><circle cx="10" cy="10" r="8" fill="none" stroke="var(--blue-deep)" stroke-width="1.8"/><path d="M6 10.5l3 3 6-7" fill="none" stroke="var(--blue-deep)" stroke-width="1.8"/></svg>If the behavior of an employee, manager or your entire staff is a problem</li>
  </ul>

  <p class="cta">I CAN HELP</p>

  <p class="contact">For more information contact<br>Marla Quinn on<svg viewBox="0 0 24 24"><path d="M6.6 10.8a15 15 0 006.6 6.6l2.2-2.2c.3-.3.7-.4 1-.2 1.1.4 2.3.6 3.6.6.6 0 1 .4 1 1V20c0 .6-.4 1-1 1A17 17 0 013 4c0-.6.4-1 1-1h3.5c.6 0 1 .4 1 1 0 1.3.2 2.5.6 3.6.1.3 0 .7-.2 1z" fill="#f2c230"/></svg>555-014-2275 or 555-0178</p>
</main>
</body>
</html>
```